Bespoke Builders Business Card Design

We need a business card for an established builder of high quality bespoke homes in Auckland and Northland. We build and renovate homes collaboratively facilitating effective communication between owners, builders, architects, suppliers and tradespeople. We have never built or renovated a home that leaks or has faults. We only use reliable materials. We have never been sued or had legal action taken against us. We are honest builders of bespoke homes not group mass produced homes. Our niche market is in character homes. We practice sustainability and have built a lot of coastal property. We have been in business for over thirty years . We would like to see natural colors of the environment sand,sea and maybe vegetation . The design should communicate quality, sustainability,fair pricing, open communication and the originality of bespoke building. And the fact that the builder is registered.

Business

Dale Morvick Builders
Ph. 021583917
58 Harlow Rd Kerrigan Bay Auckland 0915
PO Box 287 Tawharu 0563

```html
<!DOCTYPE html>
<html lang="en">
<head>
<meta charset="utf-8">
<title>Dale Morvick Builders – Business Card</title>
<link href="https://fonts.googleapis.com/css2?family=Open+Sans:wght@400;600;700&display=swap" rel="stylesheet">
<style>
  :root {
    --bg: #ecebe8;
    --card: #ffffff;
    --teal: #1f8ea6;
    --teal-dark: #0f6278;
    --teal-light: #74c6d4;
    --white: #ffffff;
  }
  * { box-sizing: border-box; margin: 0; padding: 0; }
  html, body {
    width: 1200px; height: 900px; overflow: hidden;
    background: var(--bg);
    font-family: "Open Sans", Arial, sans-serif;
  }
  .stage {
    width: 1200px; height: 900px;
    display: flex; align-items: center; justify-content: center; gap: 40px;
  }
  .card {
    position: relative;
    width: 560px; height: 320px;
    background: var(--card);
    overflow: hidden;
    box-shadow: 0 6px 18px rgba(0,0,0,0.15);
  }
  .card-front .wave { position: absolute; inset: 0; width: 100%; height: 100%; }
  .holder {
    position: absolute; top: 22px; right: 30px; text-align: right;
    color: var(--teal-dark);
  }
  .holder-name { font-size: 26px; font-weight: 700; line-height: 1.15; }
  .holder-title { font-size: 15px; font-weight: 400; color: var(--teal); line-height: 1.3; }
  .brand {
    position: absolute; display: flex; align-items: center; gap: 10px;
    color: var(--teal-dark); font-weight: 700;
  }
  .brand-name { line-height: 1.1; }
  .brand-dot { border-radius: 50%; background: var(--teal); flex: none; }
  .card-front .brand { left: 38px; top: 138px; font-size: 20px; }
  .card-front .brand-dot { width: 16px; height: 16px; }
  .contact {
    position: absolute; right: 30px; bottom: 28px; text-align: right;
    color: var(--white); font-size: 13px; line-height: 1.55;
  }
  .contact-phone { font-weight: 700; font-size: 15px; display: inline-flex; align-items: center; gap: 6px; }
  .contact-phone svg { width: 13px; height: 13px; }
  .card-back .brand {
    left: 0; right: 0; top: 118px; justify-content: center; font-size: 26px;
  }
  .card-back .brand-dot { width: 20px; height: 20px; }
  .tagline-band {
    position: absolute; left: 0; right: 0; bottom: 0; height: 34px;
    background: var(--teal-dark);
    display: flex; align-items: center; padding-left: 22px;
  }
  .tagline { color: var(--white); font-size: 14px; }
</style>
</head>
<body>
<main class="stage">
  <section class="card card-front">
    <svg class="wave" viewBox="0 0 560 320" preserveAspectRatio="none" aria-hidden="true">
      <defs>
        <linearGradient id="sea" x1="0" y1="1" x2="1" y2="0">
          <stop offset="0" stop-color="#74c6d4"/>
          <stop offset="0.6" stop-color="#1f8ea6"/>
          <stop offset="1" stop-color="#0f6278"/>
        </linearGradient>
      </defs>
      <path d="M160 320 C230 250 200 160 290 130 C380 100 470 110 560 90 L560 320 Z" fill="url(#sea)"/>
      <path d="M195 320 C255 255 235 175 315 148 C400 120 480 128 560 110 L560 120 C485 138 410 132 330 162 C255 190 275 260 215 320 Z" fill="#ffffff"/>
    </svg>
    <div class="holder">
      <p class="holder-name">Dale Morvick</p>
      <p class="holder-title">Title here</p>
    </div>
    <div class="brand"><span class="brand-dot"></span><span class="brand-name">Dale Morvick<br>Builders</span></div>
    <div class="contact">
      <p class="contact-phone">021583917
        <svg viewBox="0 0 24 24" aria-hidden="true"><path fill="#fff" d="M6.6 10.8a15.1 15.1 0 0 0 6.6 6.6l2.2-2.2a1 1 0 0 1 1-.25 11.4 11.4 0 0 0 3.6.6 1 1 0 0 1 1 1V20a1 1 0 0 1-1 1A17 17 0 0 1 3 4a1 1 0 0 1 1-1h3.5a1 1 0 0 1 1 1c0 1.25.2 2.45.6 3.6a1 1 0 0 1-.25 1z"/></svg>
      </p>
      <p>58 Harlow Rd Kerrigan Bay Auckland 0915</p>
      <p>PO Box 287 Tawharu 0563</p>
    </div>
  </section>

  <section class="card card-back">
    <div class="brand"><span class="brand-dot"></span><span class="brand-name">Dale Morvick Builders</span></div>
    <div class="tagline-band">
      <p class="tagline">Quality bespoke homes in Auckland and Northland</p>
    </div>
  </section>
</main>
</body>
</html>
```